Velantra Energy Commercial Solar Brochure

Create design layout, and content with our help that fully explains our commercial solar division. We want to show the process from energy analysis, value engineering, consulting, design, engineering, construction and commissioning.

We provide a production guarantee on all our commercial systems to ensure they continue to produce at maximum capacity for years to come.

We also need to explain the importance of maintenance, monitoring, and how we care for the system 24/7 including 24/7 monitoring, thermal scans, panel washing, amp/voltage checks, inverter inspections. ETC.

Target Market(s)

Farmers, Commercial Businesses, Cold Storage, Churches

Industry/Entity Type

Solar Energy

Font styles to use
Other font styles liked:
• FF DAX

Colors
3276b5

Requirements
Must have
• Must explain the Velantra Advantage - why use us. Must define the benefits of solar to commercial clients, including quality, value engineering, NEMA. Must tell the story from energy analysis, construction, maintenance, and power production guarantee.
Nice to have
• Financing sources, agricultural feel
Should not have
• negative tone

```html
<!DOCTYPE html>
<html lang="en">
<head>
<meta charset="utf-8">
<title>Velantra Energy – The Renewable Energy O&amp;M Solution</title>
<link rel="stylesheet" href="https://fonts.googleapis.com/css2?family=Open+Sans:wght@600;700&display=swap">
<style>
  :root {
    --page-bg: #e9e6e1;
    --brand-blue: #3276b5;
    --deep-blue: #1f5f9e;
    --bright-blue: #2f8fd0;
    --sky-top: #3d7fc4;
    --sky-low: #a9cbe6;
    --panel-blue: #243e78;
    --accent-orange: #e9a31f;
    --navy-text: #1d2f5e;
    --white: #ffffff;
  }
  * { box-sizing: border-box; margin: 0; padding: 0; }
  html, body { width: 1200px; height: 803px; overflow: hidden; }
  body {
    background: var(--page-bg);
    font-family: "Open Sans", Arial, sans-serif;
    display: flex;
    align-items: center;
    justify-content: center;
  }
  .brochure-cover {
    position: relative;
    width: 540px;
    height: 760px;
    overflow: hidden;
    box-shadow: 0 6px 18px rgba(0,0,0,0.18);
  }
  .cover-art { position: absolute; inset: 0; display: block; }
  .brand-tile {
    position: absolute;
    top: 0;
    right: 22px;
    width: 126px;
    height: 108px;
    background: var(--white);
    border-radius: 0 0 10px 10px;
    box-shadow: 2px 4px 8px rgba(0,0,0,0.3);
    display: flex;
    align-items: center;
    justify-content: center;
    text-align: center;
  }
  .brand-name {
    color: var(--navy-text);
    font-weight: 700;
    font-size: 19px;
    line-height: 1.1;
  }
  .cover-title {
    position: absolute;
    left: 62px;
    top: 530px;
    color: var(--white);
    font-weight: 700;
    font-size: 30px;
    line-height: 1.55;
    letter-spacing: 0.3px;
    text-transform: uppercase;
    text-shadow: 0 1px 2px rgba(0,0,0,0.25);
  }
  .web-bar {
    position: absolute;
    left: 22px;
    right: 22px;
    bottom: 22px;
    height: 58px;
    background: var(--white);
    border-radius: 12px;
    display: flex;
    align-items: center;
    justify-content: center;
  }
  .web-address {
    color: var(--navy-text);
    font-weight: 600;
    font-size: 12px;
    letter-spacing: 3px;
    text-transform: uppercase;
  }
</style>
</head>
<body>
  <section class="brochure-cover">
    <svg class="cover-art" viewBox="0 0 540 760" width="540" height="760">
      <defs>
        <linearGradient id="photoTones" x1="0" y1="0" x2="0" y2="1">
          <stop offset="0" stop-color="var(--sky-top)"/>
          <stop offset="0.42" stop-color="var(--sky-low)"/>
          <stop offset="0.5" stop-color="#5a79ad"/>
          <stop offset="1" stop-color="var(--panel-blue)"/>
        </linearGradient>
        <linearGradient id="lowerBlue" x1="0" y1="0" x2="1" y2="1">
          <stop offset="0" stop-color="var(--deep-blue)"/>
          <stop offset="0.5" stop-color="var(--bright-blue)"/>
          <stop offset="1" stop-color="var(--brand-blue)"/>
        </linearGradient>
      </defs>
      <rect class="cover-photo" x="0" y="0" width="540" height="500" fill="url(#photoTones)"
            role="img" aria-label="Photo of two technicians in safety vests walking across a large rooftop solar array under a blue sky"/>
      <path class="wave-accent" fill="var(--accent-orange)"
            d="M0 458 C80 400 170 380 250 392 C285 398 300 410 318 430 C340 380 420 330 540 300 L540 760 L0 760 Z"/>
      <path class="wave-panel" fill="url(#lowerBlue)"
            d="M0 470 C80 412 170 392 250 404 C285 410 300 422 318 444 C340 394 420 344 540 314 L540 760 L0 760 Z"/>
      <path class="wave-stitch" fill="none" stroke="var(--white)" stroke-width="1.6" stroke-dasharray="1.5 4" stroke-linecap="round"
            d="M0 480 C80 422 170 402 250 414 C285 420 300 432 318 456 C340 406 420 356 540 326"/>
    </svg>

    <div class="brand-tile">
      <span class="brand-name">Velantra<br>Energy</span>
    </div>

    <h1 class="cover-title">The Renewable<br>Energy O&amp;M Solution</h1>

    <div class="web-bar">
      <span class="web-address">www.velantraenergy.com</span>
    </div>
  </section>
</body>
</html>
```